Baby Care Print Log for Nannies and Parents- Creating a brand/style I can use across different forms

I am creating a notebook for babysitters to use to communicate with parents about the children they care for. I will be creating many different forms (emergency contacts, daily logs, shopping lists, etc.)
I need a look and feel from which to style these forms from. I am starting by designing the daily baby care log. I need a designer to take my Word doc with just text on it, and create a visual approach to make this visually appealing.
I do not want this to be extremely "babyish" with cartoon styling. I want it to be more of a professional looking style. I would like to be able to color each different document a different color palette, yet keep the similar look and feel. My logo is attached for inspiration. I use real photography across my website quillharborpages.com.
Updates
I will be re-designing my Wordpress website based on what design I like best and also will need other forms completed once I pick a design. I am hoping to work with someone who I can hire for further development needs as well. Added Saturday, February 11, 2017
Target Market(s)
Professional Parents
Industry/Entity Type
Education
Requirements
Must have
- color, pop, visual appeal
- Please use the color in my logo and any complementary colors that you think work well with it. I definitely like colored patterns, ombre, colored backgrounds, etc. I'd prefer for it not to be completely white with only pops of color here and there.
Nice to have
- My logo somewhere subtly on the form
- Photography elements
Should not have
- cartoon images of babies, etc. I use real photography across my website with the exception of my logo umbrella.

```html
<!DOCTYPE html>
<html lang="en">
<head>
<meta charset="utf-8">
<title>Quill Harbor – Daily Baby Care Log</title>
<link rel="stylesheet" href="https://fonts.googleapis.com/css2?family=Ubuntu:wght@400;500;700&display=swap">
<style>
  :root{
    --brand:#3bbfdf;
    --brand-deep:#1fa6c9;
    --tint-top:#cdeef8;
    --tint-mid:#e6f6fb;
    --tint-low:#f3fbfe;
    --panel:#c6eaf5;
    --ink:#111;
    --text:#4a4a4a;
    --white:#ffffff;
  }
  *{box-sizing:border-box;margin:0;padding:0}
  html,body{width:848px;height:1200px;overflow:hidden}
  body{
    font-family:"Ubuntu",sans-serif;color:var(--text);
    background:linear-gradient(180deg,var(--tint-top) 0%,var(--tint-mid) 38%,var(--tint-low) 100%);
  }
  .sheet{position:relative;width:848px;height:1200px}

  .field{position:absolute;height:36px;border:1.5px solid var(--brand);border-radius:6px;display:flex;overflow:hidden;background:var(--white)}
  .field__label{background:var(--brand);color:var(--white);font-size:19px;line-height:33px;padding:0 10px;width:68px}

  .brand-name{position:absolute;left:656px;top:76px;font-weight:500;font-size:25px;line-height:1;color:var(--ink);display:flex;align-items:center;gap:9px;white-space:nowrap}
  .brand-name__dot{width:20px;height:20px;border-radius:50%;background:var(--brand)}

  .section-title{position:absolute;font-weight:700;font-size:18px;color:var(--ink);text-transform:uppercase;letter-spacing:-.3px;line-height:1;white-space:nowrap}
  .icon{position:absolute}
  .col-label,.item{position:absolute;font-size:19px;line-height:1;white-space:nowrap}
  .rule{position:absolute;border-top:1.5px solid var(--brand);height:0}
  .box{position:absolute;border:1.5px solid var(--brand);background:var(--white)}

  .notes-panel{position:absolute;left:378px;top:808px;width:403px;height:339px;background:var(--panel);border-radius:8px}
  .notes-panel .rule{border-color:var(--brand-deep)}
</style>
</head>
<body>
<main class="sheet">

  <div class="field" style="left:53px;top:77px;width:285px"><span class="field__label">Name</span></div>
  <div class="field" style="left:382px;top:77px;width:215px"><span class="field__label">Date</span></div>

  <div class="brand-name"><span class="brand-name__dot"></span>Quill Harbor</div>

  <!-- Nap time -->
  <h2 class="section-title" style="left:53px;top:203px">Nap Time</h2>
  <svg class="icon" style="left:150px;top:188px" width="46" height="34" viewBox="0 0 46 34">
    <path d="M10 30a9 9 0 0 1 0-18 12 12 0 0 1 22-4 9 9 0 0 1 6 22z" fill="var(--brand)"/>
    <text x="14" y="24" font-size="11" font-weight="700" fill="#fff" font-family="Ubuntu">zzz</text>
  </svg>
  <span class="col-label" style="left:56px;top:254px">Time</span>
  <span class="col-label" style="left:125px;top:254px">How Long</span>
  <div class="rule" style="left:57px;top:302px;width:50px"></div><div class="rule" style="left:115px;top:302px;width:129px"></div>
  <div class="rule" style="left:57px;top:331px;width:50px"></div><div class="rule" style="left:115px;top:331px;width:129px"></div>
  <div class="rule" style="left:57px;top:358px;width:50px"></div><div class="rule" style="left:115px;top:358px;width:129px"></div>
  <div class="rule" style="left:57px;top:386px;width:50px"></div><div class="rule" style="left:115px;top:386px;width:129px"></div>

  <!-- Feeding -->
  <h2 class="section-title" style="left:383px;top:203px">Feeding</h2>
  <svg class="icon" style="left:470px;top:188px" width="22" height="42" viewBox="0 0 22 42">
    <rect x="7" y="1" width="8" height="6" rx="3" fill="var(--brand)"/>
    <rect x="4" y="7" width="14" height="4" fill="var(--brand)"/>
    <rect x="3" y="12" width="16" height="28" rx="3" fill="none" stroke="var(--brand)" stroke-width="2.5"/>
    <path d="M3 22h7M3 28h7M3 34h7" stroke="var(--brand)" stroke-width="2"/>
  </svg>
  <span class="col-label" style="left:379px;top:254px">Time</span>
  <span class="col-label" style="left:447px;top:254px">Milk (Type)</span>
  <span class="col-label" style="left:571px;top:254px">Water</span>
  <span class="col-label" style="left:650px;top:254px">Food</span>
  <span class="col-label" style="left:720px;top:254px">Amount</span>
  <div class="rule" style="left:378px;top:302px;width:61px"></div><div class="rule" style="left:445px;top:302px;width:118px"></div><div class="rule" style="left:569px;top:302px;width:71px"></div><div class="rule" style="left:646px;top:302px;width:62px"></div><div class="rule" style="left:714px;top:302px;width:83px"></div>
  <div class="rule" style="left:378px;top:331px;width:61px"></div><div class="rule" style="left:445px;top:331px;width:118px"></div><div class="rule" style="left:569px;top:331px;width:71px"></div><div class="rule" style="left:646px;top:331px;width:62px"></div><div class="rule" style="left:714px;top:331px;width:83px"></div>
  <div class="rule" style="left:378px;top:358px;width:61px"></div><div class="rule" style="left:445px;top:358px;width:118px"></div><div class="rule" style="left:569px;top:358px;width:71px"></div><div class="rule" style="left:646px;top:358px;width:62px"></div><div class="rule" style="left:714px;top:358px;width:83px"></div>
  <div class="rule" style="left:378px;top:386px;width:61px"></div><div class="rule" style="left:445px;top:386px;width:118px"></div><div class="rule" style="left:569px;top:386px;width:71px"></div><div class="rule" style="left:646px;top:386px;width:62px"></div><div class="rule" style="left:714px;top:386px;width:83px"></div>

  <!-- Diapers -->
  <h2 class="section-title" style="left:53px;top:451px">Diapers</h2>
  <svg class="icon" style="left:136px;top:442px" width="42" height="34" viewBox="0 0 42 34">
    <path d="M3 4h36v8c0 10-8 18-18 20C11 30 3 22 3 12z" fill="none" stroke="var(--brand)" stroke-width="2.5"/>
    <path d="M3 10h36" stroke="var(--brand)" stroke-width="2"/>
  </svg>
  <span class="col-label" style="left:54px;top:509px">Time</span>
  <span class="col-label" style="left:124px;top:509px">Wet</span>
  <span class="col-label" style="left:185px;top:509px">BM</span>
  <div class="rule" style="left:57px;top:586px;width:50px"></div><div class="box" style="left:130px;top:574px;width:24px;height:24px"></div><div class="box" style="left:187px;top:574px;width:24px;height:24px"></div>
  <div class="rule" style="left:57px;top:614px;width:50px"></div><div class="box" style="left:130px;top:602px;width:24px;height:24px"></div><div class="box" style="left:187px;top:602px;width:24px;height:24px"></div>
  <div class="rule" style="left:57px;top:643px;width:50px"></div><div class="box" style="left:130px;top:631px;width:24px;height:24px"></div><div class="box" style="left:187px;top:631px;width:24px;height:24px"></div>
  <div class="rule" style="left:57px;top:671px;width:50px"></div><div class="box" style="left:130px;top:659px;width:24px;height:24px"></div><div class="box" style="left:187px;top:659px;width:24px;height:24px"></div>
  <div class="rule" style="left:57px;top:700px;width:50px"></div><div class="box" style="left:130px;top:688px;width:24px;height:24px"></div><div class="box" style="left:187px;top:688px;width:24px;height:24px"></div>
  <div class="rule" style="left:57px;top:728px;width:50px"></div><div class="box" style="left:130px;top:716px;width:24px;height:24px"></div><div class="box" style="left:187px;top:716px;width:24px;height:24px"></div>

  <!-- Mood -->
  <h2 class="section-title" style="left:383px;top:451px">Mood</h2>
  <svg class="icon" style="left:449px;top:434px" width="42" height="42" viewBox="0 0 42 42">
    <circle cx="21" cy="21" r="18" fill="var(--white)" stroke="var(--brand)" stroke-width="2.5"/>
  </svg>
  <span class="item" style="left:376px;top:509px">Happy</span>
  <span class="item" style="left:459px;top:509px">Sad</span>
  <span class="item" style="left:517px;top:509px">Unsettled</span>
  <span class="item" style="left:628px;top:509px">Energetic</span>
  <span class="item" style="left:376px;top:549px">Tired</span>
  <span class="item" style="left:446px;top:549px">Chatty</span>
  <span class="item" style="left:524px;top:549px">Quiet</span>

  <!-- Today activities -->
  <h2 class="section-title" style="left:382px;top:628px">Today Activities</h2>
  <svg class="icon" style="left:539px;top:612px" width="32" height="42" viewBox="0 0 32 42">
    <circle cx="16" cy="13" r="11" fill="var(--brand)"/>
    <rect x="13" y="23" width="6" height="17" rx="3" fill="var(--brand)"/>
  </svg>
  <div class="rule" style="left:379px;top:677px;width:418px"></div>
  <div class="rule" style="left:379px;top:705px;width:418px"></div>
  <div class="rule" style="left:379px;top:734px;width:418px"></div>

  <!-- Supplies -->
  <h2 class="section-title" style="left:53px;top:814px">Supplies Needed Soon</h2>
  <svg class="icon" style="left:268px;top:794px" width="42" height="42" viewBox="0 0 42 42">
    <path d="M21 2v10M16 8l5 5 5-5" stroke="var(--brand)" stroke-width="2.5" fill="none"/>
    <path d="M3 18h36l-4 20H7z" fill="var(--white)" stroke="var(--brand)" stroke-width="2.5"/>
    <path d="M14 23v10M21 23v10M28 23v10" stroke="var(--brand)" stroke-width="2.5"/>
  </svg>
  <span class="item" style="left:50px;top:868px">Diapers</span><div class="box" style="left:214px;top:862px;width:33px;height:33px"></div>
  <span class="item" style="left:50px;top:911px">Diaper Cream</span><div class="box" style="left:214px;top:905px;width:33px;height:33px"></div>
  <span class="item" style="left:50px;top:953px">Milk/Formula</span><div class="box" style="left:214px;top:947px;width:33px;height:33px"></div>
  <span class="item" style="left:50px;top:996px">Wet Wipes</span><div class="box" style="left:214px;top:990px;width:33px;height:33px"></div>
  <span class="item" style="left:50px;top:1039px">Cereal</span><div class="box" style="left:214px;top:1033px;width:33px;height:33px"></div>
  <span class="item" style="left:50px;top:1082px">Baby Food</span><div class="box" style="left:214px;top:1076px;width:33px;height:33px"></div>
  <span class="item" style="left:50px;top:1124px">Others:</span><div class="rule" style="left:135px;top:1147px;width:154px"></div>

  <!-- Special notes -->
  <section class="notes-panel">
    <div class="rule" style="left:32px;top:56px;width:337px"></div>
    <div class="rule" style="left:32px;top:84px;width:337px"></div>
    <div class="rule" style="left:32px;top:113px;width:337px"></div>
    <div class="rule" style="left:32px;top:141px;width:337px"></div>
    <div class="rule" style="left:32px;top:170px;width:337px"></div>
    <div class="rule" style="left:32px;top:198px;width:337px"></div>
    <div class="rule" style="left:32px;top:226px;width:337px"></div>
    <div class="rule" style="left:32px;top:255px;width:337px"></div>
    <div class="rule" style="left:32px;top:283px;width:337px"></div>
    <div class="rule" style="left:32px;top:311px;width:337px"></div>
  </section>
  <h2 class="section-title" style="left:383px;top:814px">Special Notes</h2>
  <svg class="icon" style="left:520px;top:797px" width="42" height="40" viewBox="0 0 42 40">
    <rect x="3" y="7" width="30" height="30" rx="3" fill="var(--white)" stroke="var(--brand)" stroke-width="3"/>
    <path d="M15 25l3-7 16-16 5 5-16 16z" fill="var(--brand)"/>
  </svg>

</main>
</body>
</html>
```